International Clinical Software Company needs a new business card design

We are looking for a new business card design for our company that has recently expanded into the UK market, making us a multinational company.
After having rebranded our website and produced a new style guide, we are looking for a business card that is creative and attention grabbing, while being consistent with the style and colour scheme used on the new website, www.brookvale.example
We produce care management technology for the aged care market, but the main aspect we aim to communicate is the human element of our software, and the way it assists in providing better care for aged people, and stronger relationships between aged people and the staff that care for them.
Our current business card is a dark green with gold text, which makes the text quite difficult to read, not very aesthetically appealing and the colour scheme looks quite dated.
We would like something fresh and modern, that can still be colourful but doesn't use large blocks of dark colour, and uses the colours within our logo.
Something tying in with the leaves that are used in our logo could work quite nicely, along with the Autumn/Fall colours of soft greens, yellows and reds (also in our existing logo). However also happy to look at fresh, completely out of the box ideas we may not have yet considered.
Target Market(s)
The people that receive this business card work in the aged card or health industry and are either corporate/management level staff or clinical (Registered Nurses, care workers etc.)
Industry/Entity Type
Health Product
Contact Information for Business Card
Company Name - BrookvaleTech
Company locations: Harrowby Isles, Caldermoor, Westfell Bay
Staff Details:
Staff name: Dermot Quill
Staff job title: Executive Chairman
Staff email: d.quill@brookvale.example
Office phone number: 01632 960418
Font styles to use
Other font styles liked:
- Calibri
Requirements
Must have
- Must include the BrookvaleTech brand name in it's current font
- Must include logo (3 leaves in gold circle)
- Must include Business Card Details
Nice to have
- Elements of gold
- White space
- Something autumn themed but not too cliched
Should not have
- No blue - used by a major competitor and we would like to differentiate from them
- Large blocks of dark green colour (the green that appears in our leaves on the logo on our current business card is the background colour and it is far too dark)

```html
<!DOCTYPE html>
<html lang="en">
<head>
<meta charset="utf-8">
<title>BrookvaleTech Business Card</title>
<link rel="stylesheet" href="https://fonts.googleapis.com/css2?family=Open+Sans:wght@400;600;700&display=swap">
<style>
  :root {
    --backdrop: #3a322e;
    --card-black: #1c1c1d;
    --card-gold: #b09a6c;
    --gold: #c9a868;
    --gold-soft: #b89a62;
    --white: #ffffff;
    --text-light: #e6e6e6;
    --divider: #6e6048;
  }
  * { box-sizing: border-box; margin: 0; padding: 0; }
  html, body {
    width: 1200px;
    height: 844px;
    overflow: hidden;
    background: var(--backdrop);
    font-family: "Open Sans", Calibri, Arial, sans-serif;
  }
  .canvas {
    position: relative;
    width: 1200px;
    height: 844px;
    display: flex;
    align-items: center;
    justify-content: center;
    gap: 40px;
  }
  .card {
    position: relative;
    width: 540px;
    height: 309px;
    border-radius: 3px;
    box-shadow: 0 10px 24px rgba(0, 0, 0, 0.45);
    overflow: hidden;
  }

  /* Front */
  .card-front {
    background: var(--card-black);
    display: flex;
    align-items: center;
  }
  .brand-block {
    width: 250px;
    display: flex;
    flex-direction: column;
    align-items: center;
    gap: 16px;
    padding-top: 40px;
  }
  .brand-dot {
    width: 62px;
    height: 62px;
    border-radius: 50%;
    background: var(--gold-soft);
  }
  .brand-name {
    color: var(--gold);
    font-size: 30px;
    font-weight: 400;
    letter-spacing: 0.5px;
  }
  .divider {
    width: 1px;
    height: 150px;
    background: var(--divider);
    margin-top: -30px;
  }
  .contact-block {
    padding-left: 24px;
    margin-top: -40px;
    color: var(--text-light);
    font-size: 14px;
    line-height: 1.35;
  }
  .person-name {
    color: var(--gold);
    font-size: 18px;
    font-weight: 700;
  }
  .person-title { margin-bottom: 14px; }
  .contact-line {
    display: flex;
    align-items: center;
    gap: 8px;
    margin-bottom: 16px;
  }
  .contact-line svg { width: 11px; height: 11px; fill: var(--gold); flex: none; }

  /* Back */
  .card-back {
    background: var(--card-gold);
    display: flex;
    flex-direction: column;
    align-items: center;
    justify-content: center;
    gap: 18px;
  }
  .back-ring {
    width: 130px;
    height: 130px;
    border-radius: 50%;
    border: 5px solid var(--white);
  }
  .back-name {
    color: var(--white);
    font-size: 26px;
    font-weight: 400;
    letter-spacing: 0.5px;
  }
</style>
</head>
<body>
  <main class="canvas">
    <section class="card card-front" aria-label="Business card front">
      <div class="brand-block">
        <div class="brand-dot"></div>
        <div class="brand-name">BrookvaleTech</div>
      </div>
      <div class="divider"></div>
      <div class="contact-block">
        <div class="person-name">Dermot Quill</div>
        <div class="person-title">Executive Chairman</div>
        <div class="contact-line">
          <svg viewBox="0 0 24 24" aria-hidden="true"><path d="M6.6 10.8a15.2 15.2 0 0 0 6.6 6.6l2.2-2.2c.3-.3.7-.4 1-.2 1.1.4 2.3.6 3.6.6.6 0 1 .4 1 1V20c0 .6-.4 1-1 1A17 17 0 0 1 3 4c0-.6.4-1 1-1h3.5c.6 0 1 .4 1 1 0 1.3.2 2.5.6 3.6.1.3 0 .7-.2 1z"/></svg>
          <span>d.quill@brookvale.example</span>
        </div>
        <div class="locations">Harrowby Isles, Caldermoor<br>Westfell Bay</div>
      </div>
    </section>

    <section class="card card-back" aria-label="Business card back">
      <div class="back-ring"></div>
      <div class="back-name">BrookvaleTech</div>
    </section>
  </main>
</body>
</html>
```